Indie author needs a minimalist book cover

I need a book cover for my latest book on personal finance and investing. The book is called, "The Quiet Harvest: Methods for Steady Savings, Careful Spending, and a Calm Future". This is volume one of a three part series on the FI/RE movement, which stands for 'Financial Independence/Retire Early'. This book is on the foundational principles of FI/RE and details the specific steps that these 'Quiet Harvest' involved in this community have done to position themselves to retire from paid work and live the life of their dreams - many only in their 20's, 30's and early 40's.

Title: The Quiet Harvest
Author: PK Brenner
Volume 1: Foundations
Book dimensions: 6"x9"

Book Blurb (for back cover):

Let's face it, no one wants to be different. But sometimes following the 'normal' crowd gets you no further than that crowd.

When it comes to money, the normal crowd is your typical consumer. Deep in debt, struggling to make ends meet, but still spending money on the newest 'thing' that just came out.

But there's another group that's been forming - right on the fringes of the personal finance world. I call them The Quiet Harvest. This book is about these superheroes of personal finance.

In it, you will learn:
• Who The Quiet Harvest are and what is this FI/RE Movement they are apart of
• What basic strategy they use to control their money
• How they became debt-free - and how you can join them
• How to use the SP/CE Lever to help you really move the needle towards financial independence
• How to diversify your income with a side-hustle and which one to choose
• The money outlier savings plan that will allow you to reach financial independence in ten years or less

This first book in The Quiet Harvest series is about building a solid foundation so you and your family can become Quiet Harvest, reach financial freedom, retire early, and live a rich life.

Target Market(s)

Individuals looking to take control of their money, reach financial independence, and retire early.

Font styles to use
Sans Serif
Other font styles liked:
• Arvo

Colors

Designer to choose colors to be used in the design.

Requirements
Must have
• A minimalist design (see examples), the title of the book, my author name, and the volume number and name (see below).
• My vision for the cover is to have a way to represent an 'outlier' in a simple, minimalistic way. I'm not set on any specific design - I'm open to what the designers come up with; I don't want to hold back anyone's creativity.
• Title: The Quiet Harvest
• Author: PK Brenner
• Volume 1: Foundations
• Book Blurb (for back cover):
• Let's face it, no one wants to be different. But sometimes following the 'normal' crowd gets you no further than that crowd.
• When it comes to money, the normal crowd is your typical consumer. Deep in debt, struggling to make ends meet, but still spending money on the newest 'thing' that just came out.
• But there's another group that's been forming - right on the fringes of the personal finance world. I call them The Quiet Harvest. This book is about these superheroes of personal finance.
• In it, you will learn:
• • Who The Quiet Harvest are and what is this FI/RE Movement they are apart of
• • What basic strategy they use to control their money
• • How they became debt-free - and how you can join them
• • How to use the SP/CE Lever to help you really move the needle towards financial independence
• • How to diversify your income with a side-hustle and which one to choose
• • The money outlier savings plan that will allow you to reach financial independence in ten years or less
• This first book in The Quiet Harvest series is about building a solid foundation so you and your family can become Quiet Harvest, reach financial freedom, retire early, and live a rich life.
Nice to have
• The subtitle - but only if it's not too crowded. Like I said before, I'm more interested in maintaining a minimalist aesthetic.
• The subtitle is: "Methods for Steady Savings, Careful Spending, And A Calm Future"
Should not have
• Too many colors or objects on the cover.

```html
<!DOCTYPE html>
<html lang="en">
<head>
<meta charset="utf-8">
<title>The Quiet Harvest — Volume 1: Foundations — PK Brenner</title>
<link href="https://fonts.googleapis.com/css2?family=Open+Sans:wght@400;600;700&family=Tinos:wght@700&display=swap" rel="stylesheet">
<style>
  :root {
    --backdrop: #d6ebf6;
    --paper: #ffffff;
    --gold: #dc9c12;
    --ink: #3d3a35;
    --ink-soft: #4a4742;
    --trail-red: #e0261a;
  }
  html, body {
    margin: 0;
    width: 1200px;
    height: 1200px;
    overflow: hidden;
    background: var(--backdrop);
  }
  .cover {
    position: absolute;
    left: 240px;
    top: 47px;
    width: 722px;
    height: 1081px;
    background: var(--paper);
    overflow: hidden;
    font-family: "Open Sans", sans-serif;
  }
  .volume-tab {
    position: absolute;
    left: 488px;
    top: 0;
    width: 144px;
    height: 143px;
    background: var(--gold);
    border-radius: 0 0 8px 8px;
    color: var(--paper);
    font-family: "Tinos", "Times New Roman", serif;
    font-weight: 700;
    text-align: center;
  }
  .volume-tab .volume-label {
    position: absolute;
    top: 56px;
    left: 0;
    right: 0;
    font-size: 18px;
    line-height: 1;
  }
  .volume-tab .volume-number {
    font-size: 40px;
    vertical-align: -2px;
    margin-left: 2px;
  }
  .volume-tab .volume-name {
    position: absolute;
    top: 102px;
    left: 0;
    right: 0;
    font-size: 17px;
    line-height: 1;
  }
  .title-block {
    position: absolute;
    right: 116px;
    top: 166px;
    text-align: right;
    margin: 0;
    font-weight: 600;
  }
  .title-article {
    display: block;
    font-size: 50px;
    line-height: 1;
    color: var(--ink);
    letter-spacing: -1px;
    margin-bottom: 6px;
  }
  .title-line {
    display: block;
    font-size: 114px;
    line-height: 114px;
    letter-spacing: -3px;
  }
  .title-line.first { color: var(--gold); }
  .title-line.second { color: var(--ink); margin-top: 2px; }
  .subtitle {
    position: absolute;
    right: 126px;
    top: 456px;
    margin: 0;
    text-align: right;
    font-size: 20px;
    line-height: 30px;
    color: var(--ink-soft);
    text-transform: uppercase;
  }
  .subtitle .lead { font-weight: 700; color: var(--ink); }
  .author {
    position: absolute;
    right: 124px;
    top: 606px;
    margin: 0;
    font-size: 48px;
    font-weight: 700;
    color: var(--ink);
    letter-spacing: -0.5px;
  }
  .outlier-mark {
    position: absolute;
    left: 506px;
    top: 714px;
    font-size: 128px;
    font-weight: 700;
    line-height: 1;
    color: var(--gold);
  }
  .crowd-trail {
    position: absolute;
    left: 0;
    top: 0;
  }
</style>
</head>
<body>
  <main class="cover">
    <svg class="crowd-trail" width="722" height="1081" viewBox="0 0 722 1081" role="img" aria-label="A dense trail of small red dollar signs running diagonally down across the cover, the crowd">
      <polygon points="0,515 0,590 722,1050 722,990" fill="var(--trail-red)" opacity="0.85"/>
    </svg>

    <div class="volume-tab">
      <div class="volume-label">Volume <span class="volume-number">1</span></div>
      <div class="volume-name">Foundations</div>
    </div>

    <h1 class="title-block">
      <span class="title-article">The</span>
      <span class="title-line first">QUIET</span>
      <span class="title-line second">HARVEST</span>
    </h1>

    <p class="subtitle">
      <span class="lead">Methods for</span><br>
      Steady Savings, Careful<br>
      Spending,<br>
      And A Calm Future
    </p>

    <p class="author">PK BRENNER</p>

    <div class="outlier-mark" aria-hidden="true">$</div>
  </main>
</body>
</html>
```